Yard Waste Graphic

Need to have a graphic showing yard waste that we can post on materials and on our website. A simple graphic showing some 30 gallon biodegradable bags, and a bundle of brush that's no longer than 4 feet in length. I'll attach the guidelines. Like picture but without the carts. Here is more info. https://www.brinmoorvale.example/gov/departments/pw/spring_yard_collection.asp

```html
<!DOCTYPE html>
<html lang="en">
<head>
<meta charset="utf-8">
<title>Spring Yard Waste</title>
<link href="https://fonts.googleapis.com/css2?family=Jost:wght@400&family=Arimo:wght@400&display=swap" rel="stylesheet">
<style>
  :root {
    --navy: #0d3f8c;
    --red: #a3282a;
    --ink: #111111;
    --paper: #ffffff;
    --backdrop: #e9ebee;
    --bloom-light: #fbf3f6;
    --bloom-pink: #efc3d3;
  }
  html, body {
    margin: 0;
    padding: 0;
    width: 1200px;
    height: 923px;
    overflow: hidden;
    background: var(--backdrop);
  }
  .stage {
    position: relative;
    width: 1200px;
    height: 923px;
  }
  .card {
    position: absolute;
    left: 0;
    top: 100px;
    width: 1050px;
    height: 632px;
    transform: scale(1.142857);
    transform-origin: 0 0;
    background: var(--paper);
    overflow: hidden;
    font-family: "Arimo", Arial, sans-serif;
    color: var(--ink);
  }
  .artwork {
    position: absolute;
    inset: 0;
  }
  .title-band {
    position: absolute;
    left: 0;
    top: 0;
    width: 405px;
    height: 75px;
    background: var(--navy);
    border-bottom-right-radius: 14px;
  }
  .title-band h1 {
    margin: 0;
    padding: 4px 0 0 10px;
    font-family: "Jost", "Futura", sans-serif;
    font-weight: 400;
    font-size: 50px;
    letter-spacing: -0.5px;
    color: var(--paper);
    line-height: 66px;
  }
  .section-head {
    position: absolute;
    display: flex;
    align-items: center;
    gap: 9px;
    font-family: "Jost", "Futura", sans-serif;
    font-weight: 400;
    font-size: 29px;
    color: var(--navy);
    margin: 0;
  }
  .section-head svg { flex: none; }
  .accepted-head { left: 419px; top: 10px; }
  .unaccepted-head { left: 740px; top: 9px; }
  .rules {
    position: absolute;
    margin: 0;
    padding: 0;
    list-style: none;
    font-size: 15.6px;
    line-height: 19.8px;
  }
  .rules li {
    padding-left: 9px;
    text-indent: -9px;
  }
  .accepted-list { left: 450px; top: 55px; width: 270px; }
  .unaccepted-list { left: 759px; top: 54px; width: 290px; }
  .prep-band {
    position: absolute;
    left: 455px;
    top: 246px;
    width: 595px;
    height: 49px;
    background: var(--navy);
    display: flex;
    align-items: center;
    justify-content: center;
    gap: 10px;
    padding-left: 20px;
    box-sizing: border-box;
  }
  .prep-band h2 {
    margin: 0;
    font-family: "Jost", "Futura", sans-serif;
    font-weight: 400;
    font-size: 31px;
    color: var(--paper);
  }
  .prep-list {
    left: 480px;
    top: 303px;
    width: 560px;
  }
  .prep-list li { padding-left: 0; text-indent: 0; }
</style>
</head>
<body>
<main class="stage">
  <article class="card">
    <svg class="artwork" width="1050" height="632" viewBox="0 0 1050 632">
      <defs>
        <radialGradient id="bloom" cx="0.45" cy="0.45" r="0.7">
          <stop offset="0" stop-color="var(--bloom-light)"/>
          <stop offset="1" stop-color="var(--bloom-pink)"/>
        </radialGradient>
      </defs>
      <path role="img" aria-label="Two brown paper garden waste bags filled with greenery and twigs, resting on a bundle of branches and pine cones in front of pink spring blossoms"
            d="M0,75 L392,75 C448,200 468,420 302,632 L0,632 Z" fill="url(#bloom)"/>
      <path d="M388,75 C444,200 462,420 298,632" fill="none" stroke="var(--red)" stroke-width="5"/>
      <path d="M403,75 C460,200 480,420 316,632" fill="none" stroke="var(--navy)" stroke-width="8"/>
    </svg>

    <header class="title-band">
      <h1>Spring Yard Waste</h1>
    </header>

    <h2 class="section-head accepted-head">
      <svg width="38" height="38" viewBox="0 0 38 38" aria-hidden="true">
        <circle cx="19" cy="19" r="16" fill="none" stroke="var(--navy)" stroke-width="3"/>
        <path d="M10,19 L17,27 L34,4" fill="none" stroke="var(--navy)" stroke-width="5" stroke-linejoin="round"/>
      </svg>
      Accepted Material
    </h2>
    <ul class="rules accepted-list">
      <li>- Acorns, Dead plants, Dethatching material .</li>
      <li>- Flower and vegetable bed debris (cornstalks, tomato plants etc.)</li>
      <li>- Leaves, Pine needles, Pinecones, Twigs, Weeds.</li>
      <li>- Grass clippings combined with the above materials.</li>
    </ul>

    <h2 class="section-head unaccepted-head">
      <svg width="38" height="38" viewBox="0 0 38 38" aria-hidden="true">
        <circle cx="19" cy="19" r="16" fill="none" stroke="var(--navy)" stroke-width="3"/>
        <path d="M7,7 L31,31 M31,7 L7,31" fill="none" stroke="var(--navy)" stroke-width="6" stroke-linecap="round"/>
      </svg>
      Unaccepted Material
    </h2>
    <ul class="rules unaccepted-list">
      <li>- Yard waste placed in plastic bags, trash cans, cardboard boxes, bundles tied with wire or in other containers.</li>
      <li>- Paper leaf bags containing branches, trash, grass, soil, rocks, bulky or metal tems will not be collected.</li>
      <li>- Bags with grass clippings only can not be collected.</li>
    </ul>

    <section class="prep-band">
      <svg width="40" height="40" viewBox="0 0 40 40" aria-hidden="true">
        <circle cx="20" cy="20" r="18" fill="none" stroke="var(--paper)" stroke-width="2.5"/>
        <rect x="18" y="8" width="4" height="17" rx="1.5" fill="var(--paper)"/>
        <circle cx="20" cy="30" r="2.5" fill="var(--paper)"/>
      </svg>
      <h2>How to Prepare for Collection</h2>
    </section>
    <ul class="rules prep-list">
      <li>- Use only yard waste 30 gallon biodegradable paper bags.</li>
      <li>- Grass clippings must be combined with other material. Remove dirt from roots.</li>
      <li>- Do not mix fruits, vegetables, trash, or animal droppings with your yard waste.</li>
      <li>- Do not overload yard waste bags.&nbsp; Bags must weigh less than 40 pounds.</li>
      <li>- Do not use plastic bags or cardboard boxes for yard waste.</li>
      <li>- Dirt and sod are not acceptable as yard waste.</li>
      <li>- No seasonal decoration made with wire frames and plastic materials.</li>
      <li>- Tree limbs, brush, debris must be cut into 4-foot lengths and bundled using biodegradable material and must weigh less than 40 pounds.</li>
      <li>-Yard waste should never be blown or swept into the street</li>
      <li>-Close your bags by folding them down</li>
      <li>-Bundle branches and brush up to 4 inches in diameter and 4 feet in length with organic twine (wire, nylon or plastic twine not allowed)</li>
      <li>-Place your bags at the curb on your trash day by 6 a.m.</li>
    </ul>
  </article>
</main>
</body>
</html>
```